Premium Personal Brand — Facebook Banner (Used Across All Platforms)

Update — Additional Color Direction
In addition to the dark charcoal/slate direction already described, I'm also interested in seeing variants with:
Dark navy blue — Deep, authoritative, intelligence-community feel. Same textured/matte treatment, not flat or bright.
Warm charcoal with steel blue accent — Keep the dark base but introduce a subtle steel blue gradient, accent line, or tonal shift. Sophisticated, modern, adds dimension without adding color noise.
Both should maintain the same premium, restrained, architectural feel described in the original brief. No bright blues, no corporate PowerPoint energy — think midnight, think depth, think weight.
Everything else in the brief remains the same.
I am building a premium personal brand as an executive advisor to founders ($5M+ revenue).
This contest is Facebook-banner–focused, but the design must represent a visual system that will be reused across:
- LinkedIn
- YouTube
I- nstagram
- X (Twitter)
- Website hero sections and other brand touchpoints
Think of the Facebook banner as the primary expression of the brand — not a one-off graphic.
This project is about discovering a high-end visual style and brand feel, not decoration.
What to design
Please submit one cohesive visual system, shown primarily as:
- Facebook banner (primary focus)
The same design language should clearly translate to all platforms listed above.
Designers are responsible for using the current recommended dimensions for each platform.
Quick clarification on background direction:
Backgrounds should have depth and texture, not flat color fields. Avoid pure white, light grey, or solid black backgrounds. Think matte, architectural materials — stone, graphite, concrete, steel — not blank canvases. Subtle tonal variation is encouraged. Obvious gradients or decorative patterns are not.
Text to use
Primary Headline:
- Your Business Is Too Valuable To Be Run On Hope.
Subheadline:
- You didn’t build a business to become its prisoner.
Name:
Paul Whitaker
The headline should be the dominant visual element.
Logo note (important)
My personal logo is currently being finalized.
For this contest:
- Use a simple “PW” monogram placeholder
- Clean, bold, geometric sans-serif
- Do not design a logo
- The winning design must allow an easy logo swap later.
Headshot note (important)
- Please do not include a headshot in the banner design.
- Most platforms display a circular profile image separately.
- The banner should stand on its own using typography, layout, and tone only.
- Design the banner assuming the profile photo will sit nearby, not inside the banner.
Style direction
The design should feel:
- Premium
- Calm
- Confident
- Restrained
- High-trust
- Dark, neutral backgrounds are preferred.
- Fewer elements are better than more.
Think:
- Owner-level advisor
- Private equity / boardroom tone
- Industrial, Modern, Minimalist, Elite, Architectural, not decorative
What to avoid
Please do not submit designs that feel:
- Promotional, hype-driven, or salesy
- Like a coach, guru, or agency
- Bright, colorful, or gradient-heavy
- Busy or over-designed
- Based on stock photos
- No motivational speaker energy.
Reaction test
- If someone sees this banner on Facebook (or later on LinkedIn, YouTube, etc.), the reaction should be:
“That person is serious. I’d trust them with important decisions.”
Final note
- I am not looking for many variations.
- I am looking for one strong visual direction you believe in.
Simple beats clever.
- Restraint beats decoration.

```html
<!DOCTYPE html>
<html lang="en">
<head>
<meta charset="utf-8">
<title>Paul Whitaker — Banner</title>
<link href="https://fonts.googleapis.com/css2?family=Fira+Sans:wght@400;500&display=swap" rel="stylesheet">
<style>
  :root {
    --navy-deep: #070b24;
    --navy-mid: #16206a;
    --navy-glow: #2a3a92;
    --headline: #f1efec;
    --subhead: #b3b3c8;
    --name: #e6e6ee;
    --streak: #8fb4ff;
    --figure-top: #1d2a78;
    --figure-bottom: #0d1440;
  }
  * { margin: 0; padding: 0; box-sizing: border-box; }
  html, body { width: 1200px; height: 800px; overflow: hidden; background: var(--navy-deep); }
  .banner {
    position: relative;
    width: 1200px;
    height: 800px;
    overflow: hidden;
    background:
      radial-gradient(ellipse 620px 480px at 860px 300px, var(--navy-glow) 0%, var(--navy-mid) 45%, transparent 100%),
      radial-gradient(ellipse 900px 700px at 500px 380px, #121a55 0%, var(--navy-deep) 100%);
    font-family: "Fira Sans", sans-serif;
  }
  .streak { position: absolute; inset: 0; width: 1200px; height: 800px; }
  .portrait {
    position: absolute;
    left: 510px;
    top: 32px;
    width: 630px;
    height: 768px;
    border-radius: 220px 220px 0 0;
    background: linear-gradient(180deg, var(--figure-top) 0%, var(--figure-bottom) 100%);
    opacity: 0.85;
  }
  .headline {
    position: absolute;
    left: 93px;
    top: 172px;
    font-weight: 500;
    font-size: 58px;
    line-height: 74px;
    color: var(--headline);
    letter-spacing: -0.3px;
    text-shadow: 0 2px 8px rgba(0,0,0,0.35);
  }
  .subhead {
    position: absolute;
    left: 93px;
    top: 412px;
    font-weight: 400;
    font-size: 27px;
    line-height: 50px;
    color: var(--subhead);
  }
  .signature {
    position: absolute;
    left: 338px;
    top: 588px;
    display: flex;
    align-items: center;
    gap: 14px;
    color: var(--name);
    font-weight: 500;
  }
  .signature-name {
    font-size: 21px;
    letter-spacing: 4px;
    text-transform: uppercase;
  }
  .monogram {
    width: 60px;
    height: 54px;
    border: 1px solid rgba(230,230,238,0.6);
    background: #0f1640;
    display: flex;
    align-items: center;
    justify-content: center;
    font-size: 26px;
    letter-spacing: 1px;
  }
</style>
</head>
<body>
  <div class="banner">
    <svg class="streak" viewBox="0 0 1200 800" aria-hidden="true">
      <defs>
        <filter id="streak-glow" x="-10%" y="-50%" width="120%" height="200%">
          <feGaussianBlur stdDeviation="3"/>
        </filter>
      </defs>
      <path d="M0 740 Q 520 640 1200 450" fill="none" stroke="var(--streak)" stroke-width="4" opacity="0.55" filter="url(#streak-glow)"/>
      <path d="M0 740 Q 520 640 1200 450" fill="none" stroke="#d8e6ff" stroke-width="1.2" opacity="0.8"/>
    </svg>

    <div class="portrait" role="img" aria-label="Portrait of the advisor in a navy blazer standing behind a round white table"></div>

    <h1 class="headline">Your Business Is Too<br>Valuable To Be<br>Run On Hope.</h1>
    <p class="subhead">You didn’t build a business<br>to become its prisoner.</p>

    <div class="signature">
      <span class="signature-name">Paul Whitaker</span>
      <span class="monogram">PW</span>
    </div>
  </div>
</body>
</html>
```